Brisk Fixworks business card

I need business card for my business, I think you have all my details.six months ago I design with you car wrap design. We would like to design both side of the card. On front of card we would like logo , Name and our contact details.
At the back we are looking to mentioned our services.
The name will be:
Gulbadin Norzai
Managing Director
Ph:07955384217
Email:info@brisk-fixworks.com
Web:www.brisk-fixworks.com
So we have our logo, you don’t need to change the logo.
Please see the attachment.
Thanks

Target Market(s)

Home improvement

Industry/Entity Type

Home Improvement

Contact Information for Business Card

Company name: Brisk Fixworks
Name: Gulbadin Norzai
Position: Director
Ph:07955384217
Web: www.brisk-fixworks.com
Add: 14 Garwick Lane
Hounslow
TW3 9QL
SECOND PERSON
Nasrullah norzai
Position: Handyman
Ph: 07822 643157
Email: info@brisk-fixworks.com
Add: 62 Bramcote Vale Drive
Hounslow
TW7 2KD

```html
<!DOCTYPE html>
<html lang="en">
<head>
<meta charset="utf-8">
<title>Brisk Fixworks — Business Card</title>
<link rel="stylesheet" href="https://fonts.googleapis.com/css2?family=Montserrat:wght@500;600;700;800&display=swap">
<style>
  :root {
    --navy: #253a85;
    --red: #e21f2e;
    --white: #ffffff;
    --stage: #2b2b2e;
  }
  * { box-sizing: border-box; margin: 0; padding: 0; }
  html, body { width: 1200px; height: 900px; overflow: hidden; }
  body {
    background: var(--stage);
    font-family: "Montserrat", sans-serif;
    position: relative;
  }
  .card {
    position: absolute;
    left: 250px;
    width: 700px;
    height: 400px;
    border-radius: 26px;
    overflow: hidden;
    box-shadow: 0 10px 30px rgba(0,0,0,.45);
  }
  .card-front { top: 33px; background: var(--white); }
  .card-back { top: 467px; background: var(--navy); }

  /* Front: plain straight side bands */
  .front-band-red {
    position: absolute; left: 0; top: 0; bottom: 0; width: 26px;
    background: var(--red);
  }
  .front-band-navy {
    position: absolute; left: 26px; top: 0; bottom: 0; width: 10px;
    background: var(--navy);
  }
  .front-rule {
    position: absolute; left: 36px; right: 0; bottom: 0; height: 10px;
    background: var(--navy);
  }

  .contact {
    position: absolute;
    left: 72px;
    top: 118px;
    color: var(--navy);
    white-space: nowrap;
  }
  .contact-name { font-weight: 800; font-size: 21px; letter-spacing: .5px; text-transform: uppercase; }
  .contact-role { font-weight: 700; font-size: 15px; color: var(--red); text-transform: uppercase; margin-top: 1px; }
  .contact-phone { font-weight: 800; font-size: 21px; margin-top: 8px; letter-spacing: .5px; }
  .contact-list { list-style: none; margin-top: 6px; }
  .contact-list li {
    display: flex; align-items: flex-start; gap: 9px;
    font-weight: 500; font-size: 14.5px; line-height: 1.35;
    margin-bottom: 3px;
  }
  .contact-icon { flex: 0 0 18px; width: 18px; height: 18px; margin-top: 1px; }

  .brand {
    position: absolute;
    right: 48px;
    top: 58px;
    display: flex;
    align-items: center;
    gap: 12px;
    white-space: nowrap;
  }
  .brand-mark { width: 20px; height: 20px; background: var(--red); }
  .brand-name { font-weight: 800; font-size: 30px; color: var(--navy); text-transform: uppercase; letter-spacing: .5px; }

  .tagline {
    position: absolute;
    right: 48px;
    bottom: 42px;
    text-align: right;
    font-weight: 800;
    font-size: 15px;
    line-height: 1.3;
    color: var(--navy);
    text-transform: uppercase;
  }

  /* Back: plain straight block */
  .back-block-red {
    position: absolute; left: 0; top: 0; bottom: 0; width: 150px;
    background: var(--red);
  }
  .back-block-white {
    position: absolute; left: 150px; top: 0; bottom: 0; width: 8px;
    background: var(--white);
  }
  .services {
    position: absolute;
    left: 200px;
    top: 58px;
    list-style: none;
    color: var(--white);
    font-weight: 800;
    text-transform: uppercase;
    line-height: 1.04;
    white-space: nowrap;
  }
  .services li:nth-child(1) { font-size: 17px; }
  .services li:nth-child(2) { font-size: 18px; }
  .services li:nth-child(3) { font-size: 21px; }
  .services li:nth-child(4) { font-size: 19px; }
  .services li:nth-child(5) { font-size: 25px; }
  .services li:nth-child(6) { font-size: 29px; }
  .services li:nth-child(7) { font-size: 30px; }
  .services li:nth-child(8) { font-size: 26px; }
  .services li:nth-child(9) { font-size: 26px; }
  .divider {
    position: absolute;
    left: 440px; top: 48px;
    width: 1.5px; height: 200px;
    background: var(--white);
  }
  .benefits {
    position: absolute;
    left: 462px;
    top: 62px;
    list-style: none;
    color: var(--white);
    font-weight: 700;
    font-size: 13px;
    line-height: 1.9;
    text-transform: uppercase;
    white-space: nowrap;
  }
  .benefits li::before { content: "•"; margin-right: 8px; }
</style>
</head>
<body>

<section class="card card-front" aria-label="Card front">
  <span class="front-band-red" aria-hidden="true"></span>
  <span class="front-band-navy" aria-hidden="true"></span>
  <span class="front-rule" aria-hidden="true"></span>

  <div class="contact">
    <p class="contact-name">Gulbadin Norzai</p>
    <p class="contact-role">Director</p>
    <p class="contact-phone">07955384217</p>
    <ul class="contact-list">
      <li>
        <svg class="contact-icon" viewBox="0 0 18 18" aria-hidden="true"><circle cx="9" cy="9" r="9" fill="var(--red)"/><rect x="4.5" y="5.8" width="9" height="6.4" fill="none" stroke="var(--white)" stroke-width="1.3"/><path d="M4.5 5.8L9 9.6l4.5-3.8" fill="none" stroke="var(--white)" stroke-width="1.3"/></svg>
        info@brisk-fixworks.com
      </li>
      <li>
        <svg class="contact-icon" viewBox="0 0 18 18" aria-hidden="true"><circle cx="9" cy="9" r="9" fill="var(--red)"/><circle cx="9" cy="9" r="4.6" fill="none" stroke="var(--white)" stroke-width="1.2"/><ellipse cx="9" cy="9" rx="2" ry="4.6" fill="none" stroke="var(--white)" stroke-width="1.1"/><path d="M4.4 9h9.2" stroke="var(--white)" stroke-width="1.1"/></svg>
        www.brisk-fixworks.com
      </li>
      <li>
        <svg class="contact-icon" viewBox="0 0 18 18" aria-hidden="true"><circle cx="9" cy="9" r="9" fill="var(--red)"/><path d="M9 4a3.4 3.4 0 0 1 3.4 3.4C12.4 10 9 14 9 14S5.6 10 5.6 7.4A3.4 3.4 0 0 1 9 4z" fill="var(--white)"/><circle cx="9" cy="7.4" r="1.3" fill="var(--red)"/></svg>
        14 Garwick Lane<br>Hounslow, TW3 9QL
      </li>
    </ul>
  </div>

  <div class="brand">
    <span class="brand-mark" aria-hidden="true"></span>
    <span class="brand-name">Brisk Fixworks</span>
  </div>

  <p class="tagline">From small touch<br>ups to full day jobs<br>we fix it all for you</p>
</section>

<section class="card card-back" aria-label="Card back">
  <span class="back-block-red" aria-hidden="true"></span>
  <span class="back-block-white" aria-hidden="true"></span>

  <ul class="services">
    <li>Electrical</li>
    <li>Carpentry</li>
    <li>Plumbing</li>
    <li>Plastering</li>
    <li>Flooring</li>
    <li>Fencing</li>
    <li>Decking</li>
    <li>Painting &amp;</li>
    <li>Decorating</li>
  </ul>
  <span class="divider" aria-hidden="true"></span>
  <ul class="benefits">
    <li>Free initial advice</li>
    <li>No call out charge</li>
    <li>Guarantee arrival time</li>
  </ul>
</section>

</body>
</html>
```